Wix Website for Bookkeeper - make me stand out! :)

I would like Wix website to promote my bookkeeping business. The pages that I need to create are: Home, About, Services, For Accountants, Contact Us &
Landing Page (offering a 5 part email series called "7 Rules Every Shop Founder SHOULD learn")

I would like to offer the ability for potential clients to book a 'Open Trade Vitals Review'.

I had a logo designed on Gigwell which is supposed to look like a building/calculator - I like the concept but I'm happy to have it redsigned/new colours if you don't think it works for whatever reason.

I tried to create a website myself using a template but I'm not happy with it at all. It just looks too much like a boring bookkeeping site! Haha! https://www.ledgernookpl.com.au/
Updates

Hi All - I've seen a number of good designs but I still have an open mind. If you have not yet submitted, please do and I will give you fast feedback. Thanks, Glen

Target Market(s)

Small Business Owners

Coding

Coded - Design and coding required

Number of Pages Required

5+ page

Font styles to use
Sans Serif

Requirements
Must have
• Mobile optimised
Nice to have
• Less is more :)

```html
<!DOCTYPE html>
<html lang="en">
<head>
<meta charset="utf-8">
<title>Ledger Nook Bookkeeping – Pages</title>
<link href="https://fonts.googleapis.com/css2?family=Montserrat:wght@500;600;700;800&family=Open+Sans:wght@400;600;700&display=swap" rel="stylesheet">
<style>
:root{
  --blue:#1f6fe0;
  --blue-panel:rgba(31,111,224,.88);
  --ink:#1b1b1b;
  --footer:#1d1d1d;
  --footer-text:#bdbdbd;
  --white:#ffffff;
  --grey:#e9e9e9;
}
*{box-sizing:border-box;margin:0;padding:0}
html,body{width:735px;height:1200px;overflow:hidden;background:var(--white)}
body{font-family:"Open Sans",Arial,sans-serif;color:var(--ink);position:relative}

.page{position:absolute;left:0;width:735px;overflow:hidden}
.page--landing{top:0;height:585px}
.page--home{top:612px;height:588px;box-shadow:0 0 0 1px #e3e3e3}

/* landing hero */
.landing-hero{position:relative;height:415px}
.landing-hero .photo{position:absolute;inset:0;
  background:linear-gradient(135deg,#6b6558 0%,#a59b8a 35%,#cfc6b6 60%,#8a8274 100%)}
.landing-hero .shade{position:absolute;inset:0;background:rgba(20,20,20,.35)}
.landing-hero .content{position:relative;text-align:center;padding-top:188px}
.brand-hero{display:inline-flex;align-items:center;gap:14px;color:var(--white);
  font-family:"Montserrat",sans-serif;font-weight:700;font-size:40px;letter-spacing:.5px}
.brand-hero .mark{width:44px;height:44px;background:var(--white)}
.brand-hero small{display:block}
.hero-title{margin-top:26px;color:var(--blue);font-family:"Montserrat",sans-serif;
  font-weight:800;font-size:23px;text-transform:uppercase;letter-spacing:.3px;
  text-shadow:0 1px 3px rgba(0,0,0,.35)}
.btn{display:inline-block;background:var(--blue);color:var(--white);
  font-family:"Montserrat",sans-serif;font-weight:700;font-size:10px;
  text-transform:uppercase;letter-spacing:.3px;padding:9px 18px;border-radius:2px}
.landing-hero .btn{margin-top:16px}

/* footer */
.site-footer{background:var(--footer);color:var(--footer-text);display:grid;
  grid-template-columns:200px 115px 150px 1fr;padding:22px 32px 0 32px;position:relative}
.page--landing .site-footer{height:170px}
.page--home .site-footer{height:220px;padding-top:26px}
.foot-brand{display:flex;align-items:center;gap:8px;color:var(--white);
  font-family:"Montserrat",sans-serif;font-weight:600;font-size:17px}
.foot-brand .mark{width:16px;height:16px;background:var(--white)}
.copyright{font-size:7px;line-height:1.5;margin-top:10px;text-transform:uppercase}
.foot-col h4{color:var(--white);font-family:"Montserrat",sans-serif;font-weight:700;
  font-size:9px;text-transform:uppercase;margin-bottom:6px}
.foot-col li{list-style:none;font-size:8px;line-height:1.7}
.contact-line{display:flex;align-items:center;gap:6px;font-size:8px;margin-top:6px}
.contact-line svg{flex:none}
.socials{display:flex;gap:7px;margin-top:4px}
.socials span{width:10px;height:10px;border-radius:50%;background:var(--white)}
.page-count{position:absolute;right:30px;bottom:12px;font-size:7px}

/* home */
.site-nav{height:78px;display:flex;align-items:center;justify-content:space-between;padding:0 30px;background:var(--white)}
.brand-nav{display:flex;align-items:center;gap:10px;font-family:"Montserrat",sans-serif;
  font-weight:700;font-size:24px;color:var(--ink)}
.brand-nav .mark{width:28px;height:28px;background:var(--blue)}
.nav-links{display:flex;gap:22px;list-style:none;font-family:"Montserrat",sans-serif;
  font-weight:600;font-size:9px;text-transform:uppercase}
.nav-links .active{color:var(--blue);border-bottom:2px solid var(--blue);padding-bottom:3px}

.home-hero{position:relative;height:290px}
.home-hero .photo{position:absolute;inset:0;
  background:linear-gradient(100deg,#cfd4d8 0%,#e8ebec 40%,#b9c3cc 70%,#dde1e3 100%)}
.lead-panel{position:absolute;left:30px;top:0;bottom:0;width:230px;background:var(--blue-panel);
  padding:16px 18px;color:var(--white)}
.lead-panel h2{font-family:"Montserrat",sans-serif;font-weight:800;font-size:17px;text-transform:uppercase}
.lead-panel p{font-family:"Montserrat",sans-serif;font-weight:700;font-size:11px;text-transform:uppercase;
  text-align:center;line-height:1.35;margin:8px 0 12px}
.field{background:var(--white);color:#555;font-size:8px;height:20px;line-height:20px;padding:0 6px;margin-bottom:6px}
.field--tall{height:30px}
.lead-panel .btn{display:block;text-align:center;background:var(--footer);padding:7px 0;font-size:9px}
</style>
</head>
<body>

<section class="page page--landing">
  <div class="landing-hero">
    <div class="photo" role="img" aria-label="Photo of hands at a desk with a laptop showing bar charts, a calculator and paperwork"></div>
    <div class="shade"></div>
    <div class="content">
      <div class="brand-hero"><span class="mark"></span><span>LEDGER NOOK</span></div>
      <h1 class="hero-title">7 Rules Every Shop Founder SHOULD learn</h1>
      <a class="btn">Open Trade Vitals Review</a>
    </div>
  </div>
  <footer class="site-footer">
    <div>
      <div class="foot-brand"><span class="mark"></span>LEDGER NOOK</div>
      <p class="copyright">Copyright © 2020 Ledger Nook Pty Ltd<br>All rights reserved</p>
    </div>
    <div class="foot-col"><h4>Site Map</h4><ul><li>Home</li><li>About</li><li>Services</li><li>For Accountants</li><li>Contact Us</li></ul></div>
    <div class="foot-col"><h4>Contact Info</h4>
      <div style="font-size:8px">Harbourview, Western Australia</div>
      <div class="contact-line"><svg width="8" height="8" viewBox="0 0 10 10"><path d="M2 1l2 2-1 1.5c.8 1.5 1.5 2.2 3 3L7.5 6l2 2-1.5 1.5C4 9 1 6 .5 2.5z" fill="#bdbdbd"/></svg>0400 555 123</div>
      <div class="contact-line"><svg width="9" height="7" viewBox="0 0 10 7"><rect x=".5" y=".5" width="9" height="6" fill="none" stroke="#bdbdbd"/><path d="M.5.5l4.5 3.5L9.5.5" fill="none" stroke="#bdbdbd"/></svg>info@ledgernookpl.com.au</div>
    </div>
    <div class="foot-col"><h4>Follow Us</h4><div class="socials"><span></span><span></span><span></span><span></span><span></span></div></div>
    <span class="page-count">1/2</span>
  </footer>
</section>

<section class="page page--home">
  <nav class="site-nav">
    <div class="brand-nav"><span class="mark"></span>LEDGER NOOK</div>
    <ul class="nav-links"><li class="active">Home</li><li>About</li><li>Services</li><li>For Accountants</li><li>Contact Us</li></ul>
  </nav>
  <div class="home-hero">
    <div class="photo" role="img" aria-label="Photo of a man in a light shirt working through documents at an office desk with a laptop"></div>
    <form class="lead-panel">
      <h2>Save Time | Get Advice</h2>
      <p>We do the paperwork so you can focus on what matters most.</p>
      <div class="field">Name</div>
      <div class="field">Email Address</div>
      <div class="field">Phone No</div>
      <div class="field field--tall">Optional Message</div>
      <a class="btn">Open Trade Vitals Review</a>
    </form>
  </div>
  <footer class="site-footer">
    <div>
      <div class="foot-brand"><span class="mark"></span>LEDGER NOOK</div>
      <p class="copyright">Copyright © 2020 Ledger Nook Pty Ltd<br>All rights reserved</p>
    </div>
    <div class="foot-col"><h4>Site Map</h4><ul><li>Home</li><li>About</li><li>Services</li><li>For Accountants</li><li>Contact Us</li></ul></div>
    <div class="foot-col"><h4>Contact Info</h4>
      <div style="font-size:8px">Harbourview, Western Australia</div>
      <div class="contact-line"><svg width="8" height="8" viewBox="0 0 10 10"><path d="M2 1l2 2-1 1.5c.8 1.5 1.5 2.2 3 3L7.5 6l2 2-1.5 1.5C4 9 1 6 .5 2.5z" fill="#bdbdbd"/></svg>0400 555 123</div>
      <div class="contact-line"><svg width="9" height="7" viewBox="0 0 10 7"><rect x=".5" y=".5" width="9" height="6" fill="none" stroke="#bdbdbd"/><path d="M.5.5l4.5 3.5L9.5.5" fill="none" stroke="#bdbdbd"/></svg>info@ledgernookpl.com.au</div>
    </div>
    <div class="foot-col"><h4>Follow Us</h4><div class="socials"><span></span><span></span><span></span><span></span><span></span></div></div>
    <span class="page-count">2/2</span>
  </footer>
</section>

</body>
</html>
```